Fun and Splashy Flyer Design

We need a flyer designed for our new car cleaning brand! We have looked around, and the stock options either look way too dark/serious/exclusive, or they look too shiny/stock image.

We need something that can be more subtle, that works with our work van.

For this project we would like a photoshop file with individual layers, and you can just put placeholder text for the main slogan, a header 1, header 2, bullet point and body text.

What we're really looking for are the transitions between images and elements, font colours and pairings and design accents.

We want the brand to be fun, clean, happy and straightforward (slightly minimalist). Please message if you have any questions!

```html
<!DOCTYPE html>
<html lang="en">
<head>
<meta charset="utf-8">
<title>Splashline Car Care – Free Car Wash Flyer</title>
<link rel="stylesheet" href="https://fonts.googleapis.com/css2?family=Bebas+Neue&family=Montserrat:wght@600;700;800&family=Lato:wght@400;700&display=swap">
<style>
  :root {
    --teal-deep: #0c6489;
    --teal: #1479a3;
    --teal-photo-top: #4a8599;
    --teal-photo-bottom: #24677f;
    --yellow: #ffe500;
    --ink: #2f3336;
    --body: #3b3f42;
    --paper: #ffffff;
    --backdrop: #e9ecee;
  }
  * { margin: 0; padding: 0; box-sizing: border-box; }
  html, body { width: 1200px; height: 792px; overflow: hidden; background: var(--backdrop); }
  .canvas { position: relative; width: 1200px; height: 792px; }

  .flyer {
    position: absolute; left: 306px; top: 16px;
    width: 587px; height: 760px;
    background: var(--paper);
    overflow: hidden;
    box-shadow: 0 6px 24px rgba(0,0,0,.18);
    font-family: "Lato", sans-serif;
    color: var(--body);
  }
  .flyer-shapes { position: absolute; inset: 0; width: 100%; height: 100%; }

  .van-photo {
    position: absolute; left: 14px; top: 245px; width: 386px; height: 122px;
    border-radius: 40px 60px 24px 24px;
    background: linear-gradient(180deg, #f4f8fb 0%, #cfe6f5 45%, #f2e24a 78%, #d9cf3a 100%);
  }

  .brand { position: absolute; left: 14px; top: 52px; display: flex; align-items: center; gap: 8px; }
  .brand-dot { width: 30px; height: 30px; border-radius: 50%; background: var(--yellow); flex: none; }
  .brand-name {
    font-family: "Montserrat", sans-serif; font-weight: 800; font-size: 14px;
    color: var(--paper); letter-spacing: .5px; line-height: 1.15;
  }

  .headline {
    position: absolute; left: 277px; top: 37px;
    font-family: "Bebas Neue", sans-serif; font-size: 76px; line-height: 62px;
    color: var(--paper); letter-spacing: -.5px;
  }
  .headline .accent { color: var(--yellow); display: block; }

  .support { position: absolute; left: 307px; top: 376px; display: flex; align-items: center; gap: 14px; }
  .support-icon { width: 41px; height: 44px; flex: none; }
  .support-label { font-family: "Montserrat", sans-serif; font-weight: 800; font-size: 16px; color: var(--teal); letter-spacing: .6px; line-height: 18px; }
  .support-number { font-family: "Montserrat", sans-serif; font-weight: 700; font-size: 21px; color: var(--ink); line-height: 24px; }

  .about { position: absolute; left: 16px; top: 431px; width: 250px; }
  .about-kicker { font-family: "Montserrat", sans-serif; font-weight: 700; font-size: 19px; color: var(--ink); letter-spacing: 1.2px; line-height: 18px; }
  .about-title { font-family: "Montserrat", sans-serif; font-weight: 800; font-size: 34px; color: var(--teal); letter-spacing: 1.5px; line-height: 34px; }
  .about-text { margin-top: 12px; font-size: 11px; line-height: 13px; }

  .other { position: absolute; left: 16px; top: 568px; width: 250px; }
  .other-title { font-family: "Montserrat", sans-serif; font-weight: 800; font-size: 16.5px; color: var(--teal); letter-spacing: .6px; }
  .other-list { list-style: none; margin-top: 11px; }
  .other-list li { display: flex; align-items: center; gap: 10px; height: 19.8px; font-size: 10.5px; color: var(--ink); }

  .best { position: absolute; left: 307px; top: 452px; width: 260px; list-style: none; }
  .best li { display: flex; gap: 13px; height: 55.5px; }
  .best .tick { width: 18px; height: 18px; margin-top: 2px; }
  .best-title { font-family: "Montserrat", sans-serif; font-weight: 800; font-size: 13.5px; color: var(--teal); letter-spacing: .6px; line-height: 20px; }
  .best-text { font-size: 10.3px; line-height: 12px; margin-top: 3px; }

  .tick { width: 13px; height: 13px; flex: none; }

  .footer {
    position: absolute; left: 0; bottom: 0; width: 100%; height: 62px;
    background: var(--teal-deep); border-top: 5px solid var(--yellow);
    display: flex; align-items: center; padding: 0 18px; gap: 0;
    font-family: "Montserrat", sans-serif; font-weight: 600; font-size: 9.8px; color: var(--paper);
  }
  .contact { display: flex; align-items: center; gap: 10px; }
  .contact svg { width: 15px; height: 15px; flex: none; }
  .contact-email { width: 198px; }
  .contact-web { width: 216px; }
  .contact-address { line-height: 11px; }
</style>
</head>
<body>
<div class="canvas">
  <article class="flyer">
    <svg class="flyer-shapes" viewBox="0 0 1112 1440" preserveAspectRatio="none" aria-hidden="false">
      <defs>
        <linearGradient id="photoTone" x1="0" y1="0" x2="0" y2="1">
          <stop offset="0" stop-color="var(--teal-photo-top)"/>
          <stop offset="1" stop-color="var(--teal-photo-bottom)"/>
        </linearGradient>
      </defs>
      <path role="img" aria-label="Photo of a white car being washed at a car wash, toned teal"
            fill="url(#photoTone)"
            d="M0,0 H968 L1112,142 V330 C1010,470 780,610 520,690 C320,752 120,780 0,716 Z"/>
      <path fill="none" stroke="var(--yellow)" stroke-width="7"
            d="M1112,330 C1010,470 780,610 520,690 C320,752 120,780 0,716"/>
      <path fill="none" stroke="var(--yellow)" stroke-width="7" d="M968,0 L1112,142"/>
    </svg>

    <div class="van-photo" role="img" aria-label="Photo of the branded white and yellow work van with bubble graphics"></div>

    <div class="brand">
      <span class="brand-dot"></span>
      <span class="brand-name">SPLASHLINE<br>CAR CARE</span>
    </div>

    <h1 class="headline">FREE<span class="accent">CAR WASH</span>SERVICE</h1>

    <div class="support">
      <svg class="support-icon" viewBox="0 0 41 44">
        <polygon points="20.5,0 41,11 41,33 20.5,44 0,33 0,11" fill="var(--teal)"/>
        <path fill="var(--paper)" d="M15.5 13.5c.8-.6 1.8-.4 2.3.4l1.6 2.6c.4.7.3 1.6-.3 2.1l-1.2 1c.8 1.9 2.2 3.4 4 4.3l1-1.2c.5-.6 1.4-.8 2.1-.4l2.7 1.5c.8.5 1.1 1.5.6 2.3l-.9 1.5c-.7 1.1-2 1.6-3.2 1.3-5-1.3-8.9-5.3-10.1-10.3-.3-1.2.2-2.5 1.3-3.2z"/>
      </svg>
      <div>
        <div class="support-label">CALL SUPPORT</div>
        <div class="support-number">+100 555 0142</div>
      </div>
    </div>

    <section class="about">
      <h2 class="about-kicker">ABOUT OUR</h2>
      <h2 class="about-title">COMPANY</h2>
      <p class="about-text">Lorem ipsum dolor sit amet, consectetur adipiscing elit, sed do eiusmod tempor incididunt ut labore et dolore magna aliqua. consectetur adipiscing elit, sed do eiusmod</p>
    </section>

    <section class="other">
      <h3 class="other-title">OUR OTHER SERVICES</h3>
      <ul class="other-list">
        <li><svg class="tick" viewBox="0 0 20 20"><circle cx="10" cy="10" r="8.5" fill="none" stroke="var(--teal)" stroke-width="2.4"/><path d="M6 10.3l2.8 2.7L14.2 7.4" fill="none" stroke="var(--teal)" stroke-width="2.4" stroke-linecap="round" stroke-linejoin="round"/></svg>Lorem ipsum dolor sit amet, consecteture.</li>
        <li><svg class="tick" viewBox="0 0 20 20"><circle cx="10" cy="10" r="8.5" fill="none" stroke="var(--teal)" stroke-width="2.4"/><path d="M6 10.3l2.8 2.7L14.2 7.4" fill="none" stroke="var(--teal)" stroke-width="2.4" stroke-linecap="round" stroke-linejoin="round"/></svg>Lorem ipsum dolor sit amet, consecteture.</li>
        <li><svg class="tick" viewBox="0 0 20 20"><circle cx="10" cy="10" r="8.5" fill="none" stroke="var(--teal)" stroke-width="2.4"/><path d="M6 10.3l2.8 2.7L14.2 7.4" fill="none" stroke="var(--teal)" stroke-width="2.4" stroke-linecap="round" stroke-linejoin="round"/></svg>Lorem ipsum dolor sit amet, consecteture.</li>
        <li><svg class="tick" viewBox="0 0 20 20"><circle cx="10" cy="10" r="8.5" fill="none" stroke="var(--teal)" stroke-width="2.4"/><path d="M6 10.3l2.8 2.7L14.2 7.4" fill="none" stroke="var(--teal)" stroke-width="2.4" stroke-linecap="round" stroke-linejoin="round"/></svg>Lorem ipsum dolor sit amet, consecteture.</li>
      </ul>
    </section>

    <ul class="best">
      <li><svg class="tick" viewBox="0 0 20 20"><circle cx="10" cy="10" r="8.5" fill="none" stroke="var(--teal)" stroke-width="2.2"/><path d="M6 10.3l2.8 2.7L14.2 7.4" fill="none" stroke="var(--teal)" stroke-width="2.2" stroke-linecap="round" stroke-linejoin="round"/></svg>
        <div><h4 class="best-title">OUR BEST SERVICES</h4><p class="best-text">Lorem ipsum dolor sit amet, consectetur<br>adipiscing elit, sed do eiusmod tempor</p></div></li>
      <li><svg class="tick" viewBox="0 0 20 20"><circle cx="10" cy="10" r="8.5" fill="none" stroke="var(--teal)" stroke-width="2.2"/><path d="M6 10.3l2.8 2.7L14.2 7.4" fill="none" stroke="var(--teal)" stroke-width="2.2" stroke-linecap="round" stroke-linejoin="round"/></svg>
        <div><h4 class="best-title">OUR BEST SERVICES</h4><p class="best-text">Lorem ipsum dolor sit amet, consectetur<br>adipiscing elit, sed do eiusmod tempor</p></div></li>
      <li><svg class="tick" viewBox="0 0 20 20"><circle cx="10" cy="10" r="8.5" fill="none" stroke="var(--teal)" stroke-width="2.2"/><path d="M6 10.3l2.8 2.7L14.2 7.4" fill="none" stroke="var(--teal)" stroke-width="2.2" stroke-linecap="round" stroke-linejoin="round"/></svg>
        <div><h4 class="best-title">OUR BEST SERVICES</h4><p class="best-text">Lorem ipsum dolor sit amet, consectetur<br>adipiscing elit, sed do eiusmod tempor</p></div></li>
      <li><svg class="tick" viewBox="0 0 20 20"><circle cx="10" cy="10" r="8.5" fill="none" stroke="var(--teal)" stroke-width="2.2"/><path d="M6 10.3l2.8 2.7L14.2 7.4" fill="none" stroke="var(--teal)" stroke-width="2.2" stroke-linecap="round" stroke-linejoin="round"/></svg>
        <div><h4 class="best-title">OUR BEST SERVICES</h4><p class="best-text">Lorem ipsum dolor sit amet, consectetur<br>adipiscing elit, sed do eiusmod tempor</p></div></li>
    </ul>

    <footer class="footer">
      <div class="contact contact-email">
        <svg viewBox="0 0 20 20"><rect x="1.5" y="4" width="17" height="12" fill="none" stroke="var(--paper)" stroke-width="1.4"/><path d="M1.5 4.5l8.5 6.5 8.5-6.5M1.5 15.5l6-5.2M18.5 15.5l-6-5.2" fill="none" stroke="var(--paper)" stroke-width="1.4"/></svg>
        <span>hello@splashlinecare.com</span>
      </div>
      <div class="contact contact-web">
        <svg viewBox="0 0 20 20"><circle cx="10" cy="10" r="8.3" fill="none" stroke="var(--paper)" stroke-width="1.4"/><ellipse cx="10" cy="10" rx="3.6" ry="8.3" fill="none" stroke="var(--paper)" stroke-width="1.4"/><path d="M1.7 10h16.6M3 5.8h14M3 14.2h14" fill="none" stroke="var(--paper)" stroke-width="1.4"/></svg>
        <span>www.splashlinecare.com</span>
      </div>
      <div class="contact">
        <svg viewBox="0 0 20 20"><path d="M10 18.5s-6-6.2-6-10.5a6 6 0 0 1 12 0c0 4.3-6 10.5-6 10.5z" fill="none" stroke="var(--paper)" stroke-width="1.4"/><circle cx="10" cy="8" r="2.2" fill="none" stroke="var(--paper)" stroke-width="1.4"/></svg>
        <span class="contact-address">48 Harbor Lane,<br>Portland, USA 4821</span>
      </div>
    </footer>
  </article>
</div>
</body>
</html>
```